Wine Label for a White and a Red Wine from Italy

We have a very good idea of what we want with artwork. We need you to please design a 'template' with the text so we can change out the artwork from year to year. Samples are shown of what we are looking for. We are looking for options with the two basic designs. Brand name of wine is: Valora di Castegno. Both wines are in a light green Bordeaux-style bottle (note: we don't show a light green bottle in the mockup but please remember the bottle is light green). Artwork is provided. We'd like to see either the green or blue butterfly on the white wine, the red butterfly is for the red wine. Please base the design on the attached label from Brailey and/or the attached label from Chateau Mervanges.

Target Market(s)

Millennials, women

Requirements
Must have
• The artwork (butterflies) attached.
Nice to have
• Elegant, readable fonts. Please make the text so it can be changed by the printer. Please make it so the artwork can be changed too.

```html
<!DOCTYPE html>
<html lang="it">
<head>
<meta charset="utf-8">
<title>Valora di Castegno – Bianco 2018 Label</title>
<link rel="stylesheet" href="https://fonts.googleapis.com/css2?family=Cormorant+Garamond:wght@500;600&display=swap">
<style>
  :root {
    --paper: #ffffff;
    --ink: #111111;
    --rule: #b5b5b5;
    --sage: #dde5d2;
    --vintage-green: #7a9a5c;
    --art-white: #f7f8f6;
    --art-wing: #6f9048;
    --art-wing-dark: #2f4b35;
    --art-wash: #efe6d4;
  }
  * { margin: 0; padding: 0; box-sizing: border-box; }
  html, body { width: 1200px; height: 1200px; overflow: hidden; background: var(--paper); }
  body { position: relative; font-family: "Cormorant Garamond", Georgia, serif; color: var(--ink); }

  .label {
    position: absolute;
    left: 288px; top: 246px;
    width: 624px; height: 708px;
    border: 1px solid var(--rule);
    background: var(--paper);
  }
  .artwork-frame {
    position: absolute;
    left: 202px; top: -1px;
    width: 219px; height: 324px;
    background: var(--sage);
    padding: 0 8px 8px 8px;
  }
  .artwork {
    width: 100%; height: 100%;
    background:
      radial-gradient(ellipse 30% 22% at 48% 50%, var(--art-wing-dark) 0%, var(--art-wing) 45%, rgba(111,144,72,0) 100%),
      radial-gradient(ellipse 48% 38% at 45% 55%, var(--art-wash) 0%, rgba(239,230,212,0) 100%),
      var(--art-white);
  }
  .text-block { position: absolute; left: 0; right: 0; text-align: center; }

  .brand {
    top: 355px;
    font-size: 46px; font-weight: 500;
    font-variant: small-caps; letter-spacing: 0.5px;
    line-height: 1;
  }
  .cuvee { top: 434px; font-size: 25px; font-variant: small-caps; line-height: 1; }
  .vintage {
    top: 464px; font-size: 40px; font-weight: 500;
    color: var(--vintage-green);
    font-variant-numeric: oldstyle-nums; line-height: 1;
  }
  .wine-type { top: 514px; font-size: 25px; font-variant: small-caps; line-height: 1; }
  .origin { top: 546px; font-size: 25px; font-variant: small-caps; line-height: 1; }
  .producer { top: 605px; font-size: 19px; line-height: 1; }
  .producer .by { text-transform: lowercase; }
  .farming { top: 637px; font-size: 17px; line-height: 1; letter-spacing: 0.3px; }
</style>
</head>
<body>
  <main class="label">
    <div class="artwork-frame">
      <div class="artwork" role="img" aria-label="Painted green butterfly artwork on a soft white background"></div>
    </div>
    <h1 class="text-block brand">Valora di Castegno</h1>
    <p class="text-block cuvee">Barrel Select</p>
    <p class="text-block vintage">2018</p>
    <p class="text-block wine-type">Bianco</p>
    <p class="text-block origin">Piemonte, Italy</p>
    <p class="text-block producer">ARTISANLY CRAFTED <span class="by">by</span> CANTINA ALTE COLLINE</p>
    <p class="text-block farming">sustainably farmed</p>
  </main>
</body>
</html>
```